Business Card design for Brightvale Global

we need a business card design for our company. we are a trading company based in LA.

Company Name: Brightvale Global Corp.
Contact: Marla Ostrov
Title: CEO
Tel: 310-447-2093
Email: bvgcorp7@mailnest.example

Target Market(s)

International, especially China

Industry/Entity Type

Trade

Colors
3276b5
34a7d8
0555a3
0493ce
85cae6
85acd3
d0dfed
cee9f5

Requirements
Must have
• Logo and contact, to have international/global feeling

```html
<!DOCTYPE html>
<html lang="en">
<head>
<meta charset="utf-8">
<title>Brightvale Global – Business Card</title>
<link rel="stylesheet" href="https://fonts.googleapis.com/css2?family=Montserrat:wght@600;700;800&family=Questrial&display=swap">
<style>
  :root {
    --stage: #2a2b2d;
    --blue-deep: #0555a3;
    --blue-mid: #3276b5;
    --blue-bright: #0493ce;
    --blue-sky: #34a7d8;
    --blue-pale: #85cae6;
    --blue-mist: #85acd3;
    --tint-soft: #d0dfed;
    --tint-ice: #cee9f5;
    --navy-ink: #163a6b;
    --paper: #ffffff;
    --paper-shade: #eef1f5;
    --rule: #c3ccd8;
  }
  * { box-sizing: border-box; margin: 0; padding: 0; }
  html, body { width: 1200px; height: 900px; overflow: hidden; }
  body {
    background: var(--stage);
    position: relative;
    font-family: "Questrial", "Century Gothic", sans-serif;
  }
  .card {
    position: absolute;
    left: 300px;
    width: 600px;
    height: 343px;
    border-radius: 22px;
    overflow: hidden;
    box-shadow: 0 14px 30px rgba(0,0,0,0.45);
  }
  /* Front */
  .card--front {
    top: 62px;
    background: radial-gradient(ellipse at 70% 30%, var(--blue-mid) 0%, #1a6aad 45%, var(--blue-deep) 100%);
  }
  .card--front .globe-decor {
    position: absolute;
    right: -80px;
    top: 10px;
    width: 330px;
    height: 330px;
    border-radius: 50%;
    background: rgba(5, 70, 140, 0.35);
  }
  .card--front .brand {
    position: absolute;
    left: 0; right: 0;
    top: 148px;
    text-align: center;
    font-family: "Montserrat", sans-serif;
    font-weight: 700;
    font-size: 38px;
    letter-spacing: 0.5px;
    color: var(--paper);
  }
  /* Back */
  .card--back {
    top: 495px;
    background: linear-gradient(160deg, var(--paper) 0%, var(--paper) 55%, var(--paper-shade) 100%);
  }
  .card--back .globe-decor {
    position: absolute;
    right: -70px;
    top: 30px;
    width: 300px;
    height: 300px;
    border-radius: 50%;
    background: var(--tint-soft);
    opacity: 0.8;
  }
  .card--back .brand {
    position: absolute;
    left: 40px;
    top: 52px;
    display: flex;
    align-items: center;
    gap: 12px;
    font-family: "Montserrat", sans-serif;
    font-weight: 700;
    font-size: 32px;
    color: var(--blue-deep);
  }
  .brand-dot {
    width: 22px; height: 22px;
    border-radius: 50%;
    background: var(--blue-deep);
  }
  .contact-person {
    position: absolute;
    left: 40px;
    top: 190px;
  }
  .contact-name {
    font-family: "Montserrat", sans-serif;
    font-weight: 800;
    font-size: 24px;
    color: var(--navy-ink);
  }
  .contact-title {
    font-family: "Montserrat", sans-serif;
    font-weight: 700;
    font-size: 13px;
    letter-spacing: 2px;
    color: var(--blue-sky);
    margin-top: 2px;
  }
  .divider {
    position: absolute;
    left: 0;
    top: 258px;
    width: 380px;
    height: 1px;
    background: var(--rule);
  }
  .contact-lines {
    position: absolute;
    left: 40px;
    top: 270px;
    list-style: none;
    font-size: 21px;
    color: var(--navy-ink);
  }
  .contact-lines li {
    display: flex;
    align-items: center;
    gap: 10px;
    height: 30px;
  }
  .contact-icon { width: 18px; height: 18px; flex: none; }
</style>
</head>
<body>
  <section class="card card--front" aria-label="Business card front">
    <div class="globe-decor" aria-hidden="true"></div>
    <div class="brand">Brightvale Global</div>
  </section>

  <section class="card card--back" aria-label="Business card back">
    <div class="globe-decor" aria-hidden="true"></div>
    <div class="brand"><span class="brand-dot"></span>Brightvale Global</div>

    <div class="contact-person">
      <div class="contact-name">Marla Ostrov</div>
      <div class="contact-title">CEO</div>
    </div>
    <div class="divider"></div>

    <ul class="contact-lines">
      <li>
        <svg class="contact-icon" viewBox="0 0 18 18" aria-hidden="true">
          <circle cx="9" cy="9" r="8.5" fill="none" stroke="#34a7d8" stroke-width="1.4"/>
          <path d="M5.5 8.2c0-1.6 1.6-2.6 3.5-2.6s3.5 1 3.5 2.6l-1.4.5-.6-1.2H7.5l-.6 1.2z" fill="#34a7d8"/>
          <rect x="6.5" y="9.5" width="5" height="3" rx="0.8" fill="#34a7d8"/>
        </svg>
        <span>310-447-2093</span>
      </li>
      <li>
        <svg class="contact-icon" viewBox="0 0 18 18" aria-hidden="true">
          <circle cx="9" cy="9" r="8.5" fill="#34a7d8"/>
          <rect x="4.5" y="6" width="9" height="6.2" rx="0.8" fill="#ffffff"/>
          <path d="M4.8 6.4L9 9.6l4.2-3.2" fill="none" stroke="#34a7d8" stroke-width="1"/>
        </svg>
        <span>bvgcorp7@mailnest.example</span>
      </li>
    </ul>
  </section>
</body>
</html>
```